Ridgeway Patrol Website Design

Hello Designers. I am an agency and am helping a security company get a better look. I have a new logo and a car done up. We are looking for a fresh look using the blue and the gold. Open to a complimentary color.

Here is the old site
https://moravanguard.com/

Here is another design for photos and everything. We weren't sold on it because we wanted to make it simple like the first one.

https://ww2.moravanguard.com/

Attached is also the copy I would like to put on there.

I am looking for tough, competent and simple. Our customers are contruction companies, event planners etc. It has to be clean and easy.

One thing we can't provide yet is photos. We are anticipating photos of our team with arms folded beside the car, close up of the owner with a logo'd shirt on. Pictures of an Ridgeway Patrol job site etc. (which most of the time is construction. They also do Mall security. You can see if you want to use stock photos for now.

I wanted to get the look of the front page done first. Hoping for something really awesome. Have fun.

```html
<!DOCTYPE html>
<html lang="en">
<head>
<meta charset="utf-8">
<title>Ridgeway Patrol — New Brunswick's Security Professionals</title>
<link href="https://fonts.googleapis.com/css2?family=Montserrat:wght@300;400;500;700;800&family=Raleway:wght@700&family=Roboto:wght@400;500;700&display=swap" rel="stylesheet">
<style>
  :root {
    --navy: #232848;
    --navy-deep: #0e1022;
    --gold: #b08a3a;
    --gold-light: #e2bd5c;
    --hire-gold: #f0b43a;
    --ink: #1b1b1b;
    --white: #ffffff;
    --grey-text: #cfcfcf;
  }
  * { box-sizing: border-box; margin: 0; padding: 0; }
  html, body { width: 749px; height: 1200px; overflow: hidden; background: var(--white); }
  body { font-family: "Montserrat", sans-serif; color: var(--ink); }
  .page { position: relative; width: 749px; height: 1200px; overflow: hidden; }

  /* Hero */
  .hero { position: absolute; left: 0; top: 0; width: 749px; height: 313px;
    background: radial-gradient(ellipse 260px 200px at 260px 170px, #6a6a6a 0%, #3a3a3a 45%, #121212 85%), #0c0c0c; }
  .hero::after { content: ""; position: absolute; inset: 0;
    background: linear-gradient(90deg, rgba(0,0,0,0) 50%, rgba(0,0,0,0.75) 75%, #000 100%),
                linear-gradient(180deg, rgba(0,0,0,0) 70%, rgba(0,0,0,0.8) 100%); }

  .site-header { position: absolute; left: 0; top: 0; width: 749px; height: 51px; z-index: 3;
    background: linear-gradient(180deg, #2a2f52 0%, var(--navy-deep) 100%); border-radius: 0 0 6px 6px; }
  .nav-link { position: absolute; top: 18px; color: var(--white); font-size: 9.5px; font-weight: 400; }
  .nav-link .chev { display: inline-block; width: 6px; height: 4px; margin-left: 3px; vertical-align: middle; }
  .brand { position: absolute; left: 314px; top: 15px; width: 120px; text-align: center;
    display: flex; align-items: center; justify-content: center; gap: 5px;
    color: var(--gold); font-weight: 800; font-size: 11px; letter-spacing: 0.5px; }
  .brand .mark { width: 8px; height: 8px; background: var(--gold); }

  .subnav { position: absolute; top: 55px; left: 0; width: 749px; z-index: 3; }
  .subnav a { position: absolute; height: 11px; line-height: 11px; font-size: 7.5px; color: var(--white);
    background: #2f3030; border-radius: 2px 2px 0 0; text-align: center; text-decoration: none; }

  .hero-copy { position: absolute; left: 137px; top: 119px; color: var(--white); z-index: 2; }
  .hero-copy .lead { font-size: 12.5px; font-weight: 400; }
  .hero-copy h1 { font-size: 22px; font-weight: 800; letter-spacing: 1px; line-height: 26px; margin-top: 5px; }

  .contact { position: absolute; left: 477px; top: 97px; width: 135px; z-index: 2; text-align: center; color: var(--white); }
  .contact h2 { font-size: 18.5px; font-weight: 700; letter-spacing: 0.3px; }
  .contact .phone { font-family: "Roboto", sans-serif; font-size: 9px; font-weight: 300; color: #e4e4e4; margin-top: 4px; }
  .field { display: block; width: 135px; background: var(--white); border-radius: 3px; border: 1px solid #c9c9c9;
    font-family: "Roboto", sans-serif; font-size: 5.5px; color: #9a9a9a; text-align: left; padding: 3px 3px; }
  .field.name { margin-top: 9px; height: 15px; }
  .field.email { margin-top: 6px; height: 15px; }
  .field.message { margin-top: 6px; height: 51px; }
  .submit { display: block; margin: 6px 0 0 35px; width: 71px; height: 15px; border-radius: 3px;
    background: linear-gradient(180deg, #f0cf72 0%, var(--gold) 100%); color: #2a2a2a;
    font-size: 6.5px; letter-spacing: 0.5px; line-height: 15px; }

  /* Intro */
  .intro { position: absolute; top: 313px; left: 0; width: 749px; height: 208px; background: var(--white); }
  .intro p { position: absolute; left: 134px; width: 481px; text-align: center; font-size: 9.6px; line-height: 14px; font-weight: 400; color: var(--ink); }

  /* Hiring */
  .hiring { position: absolute; top: 521px; left: 0; width: 749px; height: 200px;
    background: radial-gradient(ellipse 240px 60px at 480px 100px, rgba(170,110,40,0.55), rgba(0,0,0,0) 80%),
                radial-gradient(ellipse 120px 110px at 90px 110px, #2b2f3a, rgba(0,0,0,0) 90%),
                linear-gradient(180deg, #0e0e0e 0%, #1c1a18 55%, #101218 100%); }
  .hiring h2 { position: absolute; top: 40px; width: 749px; text-align: center; font-family: "Raleway", sans-serif;
    font-weight: 700; font-size: 18px; color: var(--hire-gold); letter-spacing: 0.8px; }
  .hiring p { position: absolute; left: 140px; top: 76px; width: 469px; text-align: center; font-size: 9.4px;
    line-height: 14px; color: var(--grey-text); font-weight: 300; letter-spacing: 0.3px; }
  .hiring .more { position: absolute; left: 317px; top: 128px; width: 115px; height: 30px; border: 1px solid #d8d8d8;
    border-radius: 3px; color: var(--white); font-size: 11px; line-height: 28px; text-align: center; font-weight: 400; letter-spacing: 0.4px; }

  /* Services */
  .service { position: absolute; top: 782px; width: 109px; height: 158px; overflow: hidden; }
  .service .photo { position: absolute; inset: 0; }
  .service .label { position: absolute; left: 0; bottom: 0; width: 100%; height: 39px; background: rgba(10,10,10,0.88);
    color: var(--white); font-family: "Roboto", sans-serif; font-weight: 500; font-size: 9px; line-height: 14px;
    display: flex; align-items: center; justify-content: center; text-align: center; }

  /* Footer */
  .site-footer { position: absolute; top: 1001px; left: 0; width: 749px; height: 199px;
    background: linear-gradient(180deg, #262b4e 0%, #191c33 55%, #050608 100%); font-family: "Roboto", sans-serif; }
  .footer-phone { position: absolute; left: 137px; top: 76px; font-size: 15.5px; font-weight: 700; color: var(--gold); letter-spacing: 0.2px; }
  .footer-brand { position: absolute; left: 314px; top: 85px; width: 120px; display: flex; align-items: center; justify-content: center; gap: 5px;
    font-family: "Montserrat", sans-serif; color: var(--gold); font-weight: 800; font-size: 12px; letter-spacing: 0.5px; }
  .footer-brand .mark { width: 9px; height: 9px; background: var(--gold); }
  .footer-address { position: absolute; right: 139px; top: 77px; text-align: right; font-size: 9px; line-height: 11px; font-weight: 700; color: var(--gold); }
  .footer-rule { position: absolute; left: 22px; top: 175px; width: 705px; height: 1px; background: #7a5c22; }
  .copyright { position: absolute; top: 184px; width: 749px; text-align: center; font-size: 6px; color: var(--white); }
</style>
</head>
<body>
<div class="page">

  <section class="hero">
    <div class="hero-photo" role="img" aria-label="Black and white photo of a security officer with a radio pointing ahead"></div>
  </section>

  <header class="site-header">
    <span class="nav-link" style="left:137px">Security Services<svg class="chev" viewBox="0 0 6 4"><path d="M0.5 0.5 L3 3 L5.5 0.5" fill="none" stroke="#fff" stroke-width="0.8"/></svg></span>
    <div class="brand"><span class="mark"></span>RIDGEWAY PATROL</div>
    <span class="nav-link" style="left:542px">About Us</span>
    <span class="nav-link" style="left:592px">En<svg class="chev" viewBox="0 0 6 4"><path d="M0.5 0.5 L3 3 L5.5 0.5" fill="none" stroke="#fff" stroke-width="0.8"/></svg></span>
  </header>

  <nav class="subnav">
    <a style="left:303px;width:44px">Industries</a>
    <a style="left:353px;width:44px">Traning</a>
    <a style="left:403px;width:44px">Careers</a>
  </nav>

  <div class="hero-copy">
    <p class="lead">New Brunswick's</p>
    <h1>SECURITY<br>PROFESSIONALS</h1>
  </div>

  <form class="contact">
    <h2>CONTACT US</h2>
    <p class="phone">(506) 555-0142</p>
    <span class="field name">Name</span>
    <span class="field email">Email</span>
    <span class="field message">How we can help?</span>
    <span class="submit">SUBMIT</span>
  </form>

  <section class="intro">
    <p style="top:29px">We can meet any security need. Ridgeway Patrol is located in Dieppe, New Brunswick serving all of New Brunswick. We offer complete security services including event security, uniformed security and personal security services.</p>
    <p style="top:85px">No detail will be overlooked. Our employee training and screening process ensures that we have the right people. Our professional employees are given the tools to succeed. From crowd control to protecting people and property, our team is trained with industry best practices.</p>
    <p style="top:141px">We eliminate the guesswork for you by ensuring that we’re up-to-date on all the regulations pertaining to public safety compliance.</p>
  </section>

  <section class="hiring" role="img" aria-label="Dark background photo of a security officer's back in front of a warmly lit crowd">
    <h2>Now Hiring!</h2>
    <p>We’re looking for 10 professional part-time and full-time security officers . We want hard-working, punctual individuals that want to be part of a supportive and enriching team.</p>
    <span class="more">Read more</span>
  </section>

  <article class="service" style="left:137px">
    <div class="photo" role="img" aria-label="Retail security officer watching a store floor" style="background:linear-gradient(160deg,#8a8a8a 0%,#3a3a3a 35%,#151515 70%)"></div>
    <div class="label">RETAIL SECURITY</div>
  </article>
  <article class="service" style="left:259px">
    <div class="photo" role="img" aria-label="Worker in a hard hat reviewing a tablet on a construction site" style="background:linear-gradient(160deg,#e6e6e6 0%,#a9a59c 35%,#5d6150 70%,#2f4a26 100%)"></div>
    <div class="label">CONSTRUCTION<br>SECURITY</div>
  </article>
  <article class="service" style="left:381px">
    <div class="photo" role="img" aria-label="Event security officer with an earpiece facing a crowd" style="background:linear-gradient(160deg,#b49a90 0%,#5a4c4a 30%,#1e1f24 65%)"></div>
    <div class="label">EVENT<br>SECURITY</div>
  </article>
  <article class="service" style="left:502px">
    <div class="photo" role="img" aria-label="Close-up of an eye reflecting a screen" style="background:radial-gradient(circle at 55% 45%,#3d6e78 0%,#2c4a3c 35%,#1c2a1e 75%)"></div>
    <div class="label">INVESTIGATIONS</div>
  </article>

  <footer class="site-footer">
    <p class="footer-phone">506.555.0142</p>
    <div class="footer-brand"><span class="mark"></span>RIDGEWAY PATROL</div>
    <address class="footer-address" style="font-style:normal">412 HARBOURVIEW ST.<br>SUITE 204<br>DIEPPE NB<br>E1B 2K7</address>
    <div class="footer-rule"></div>
    <p class="copyright">Copyright 2018 · Ridgeway Patrol</p>
  </footer>

</div>
</body>
</html>
```